Quellmont Digital - WebSite Design and Hosting

Emphasis on Quellmont Digital Website Development

Prioritize the development of the website for "quellmontdigital.example" as the first and foremost project.

Client-Friendly Website Request Process
** Design the website to facilitate easy interaction for small and medium-sized business (SMB) customers who require a website.
** Include a user-friendly form that allows my customers to submit their website requirements. This form should enable customers to:
** They can Upload images and logos related to their brand.
** They can Select brand colors that align with their identity.

Provide ample space for them to add extensive information about their business and services.

Extensive Portfolio Showcase
Build a portfolio section featuring a minimum of 300 website examples. These examples should be categorized and presented in a way that makes it convenient for potential clients to sort through and select as references for their own projects.

Summary:
In summary, the primary focus is on developing "quellmontdigital.example" as the initial project. The website should be user-friendly for SMB clients, offering a form for submitting detailed requirements, including image and logo uploads and brand color selection. Additionally, an extensive portfolio with 300 website examples should be presented for clients' reference and convenience.

Target Market(s)

Small Business Owners who need a local website

Industry/Entity Type

WebDesign and hosting (A marketing agency)

Coding

Coded - Design and coding required

Number of Pages Required

5+ page

Font styles to use
Sans Serif
Script

Colors
0054AA
0677BA
7BADD7
CADEEF
E8F1F8
FFF300
FFF600
FEFA6F
FFFEC7
FFFEE8

Requirements
Must have
• Black background! My customers need a form to pick a website design package, upload logo, brand colors and description. That input must be easy to submit to Pixel Harbor to do the ProJet, we will add marketing services as well
Nice to have
• Step by step like explanaining to a 5th grader what the instructions are to get signed up. I want high tech state of the art - for SMB owners who may not be tech savvy

```html
<!DOCTYPE html>
<html lang="en">
<head>
<meta charset="utf-8">
<title>Quellmont Digital – Website Design and Hosting</title>
<link href="https://fonts.googleapis.com/css2?family=Poppins:ital,wght@0,400;0,500;0,600;0,700;0,800;0,900;1,400&display=swap" rel="stylesheet">
<style>
:root{
  --black:#000;
  --panel:#111214;
  --white:#fff;
  --yellow:#fff300;
  --blue-dark:#0054aa;
  --blue:#0677ba;
  --blue-light:#7badd7;
  --blue-pale:#cadeef;
  --blue-mist:#e8f1f8;
  --muted:#d7d7d7;
}
*{margin:0;padding:0;box-sizing:border-box}
html,body{width:1200px;height:3386px;overflow:hidden;background:var(--black)}
body{position:relative;font-family:'Poppins',sans-serif;color:var(--white)}
.abs{position:absolute}
.photo{position:absolute}

/* hero */
.hero-photo{left:0;top:0;width:1200px;height:740px;background:linear-gradient(135deg,#2d3a4a 0%,#56677c 40%,#6b7a8c 65%,#3f4e60 100%)}
.wave{position:absolute;left:0;width:1200px}
.brand{left:75px;top:48px;font-size:32px;font-weight:700;letter-spacing:.3px}
.nav{right:74px;top:58px;display:flex;gap:0;align-items:center}
.nav a{color:var(--white);text-decoration:none;font-size:14.5px;font-weight:600;padding:5px 15px}
.nav a.active{background:var(--yellow);color:#000;padding:5px 14px}
.hero-title{left:75px;top:238px;font-size:58px;font-weight:800;line-height:58px}
.hero-title .hl{color:var(--yellow)}
.hero-sub{left:75px;top:372px;width:600px;font-size:25px;font-weight:500;line-height:35px}
.btn{display:flex;align-items:center;justify-content:center;background:var(--yellow);color:#000;font-weight:700;font-size:16px}
.hero-btn{left:75px;top:461px;width:179px;height:56px}

.request{left:794px;top:142px;width:332px;height:494px;background:var(--blue-pale);border-radius:8px;padding:14px 23px}
.request h2{color:#000;font-size:33px;font-weight:700;line-height:40px;margin-bottom:14px}
.field{height:43px;background:var(--blue-mist);border:1px solid #b9cde0;margin-bottom:12px;display:flex;align-items:center;justify-content:space-between;padding:0 13px;font-size:12px;color:#222}
.field.msg{height:90px;align-items:flex-start;padding-top:14px}
.field svg{width:11px;height:11px}
.submit{height:44px;background:var(--blue-dark);color:#fff;font-weight:600;font-size:16px;display:flex;align-items:center;justify-content:center;margin-top:-3px}

/* about */
.about-frame{left:75px;top:828px;width:218px;height:230px;background:var(--yellow)}
.about-photo{left:87px;top:841px;width:499px;height:371px;background:linear-gradient(120deg,#c8d0d6 0%,#8a97a2 45%,#5f6f5e 80%,#3c6a4a 100%)}
.section-title{font-size:58px;font-weight:800;line-height:52px}
.uline{position:relative;display:inline-block}
.uline::after{content:"";position:absolute;left:-4px;right:-2px;bottom:6px;height:8px;background:var(--blue);z-index:-1}
.about-title{left:622px;top:828px;z-index:2}
.about-text{left:622px;top:945px;width:500px;font-size:13.5px;line-height:30.5px}
.about-btn{left:622px;top:1159px;width:177px;height:55px}

/* portfolio */
.portfolio-bg{left:0;top:1230px;width:1200px;height:1222px;background:var(--panel)}
.pf-title{left:0;top:1456px;width:1200px;text-align:center}
.tabs{left:258px;top:1548px;display:flex;gap:15px}
.tab{width:159px;height:48px;border:1px solid #8a8a8a;display:flex;align-items:center;justify-content:center;font-size:16px}
.tab.on{border-color:var(--yellow);color:var(--yellow)}
.card{position:absolute;width:330px}
.card .shot{width:330px;height:246px}
.card h3{font-size:20px;font-weight:700;margin-top:24px}
.card.sel .shot{border:5px solid var(--yellow);position:relative}
.overlay{position:absolute;inset:0;background:rgba(6,119,186,.55);display:flex;align-items:center;justify-content:center}
.more{background:var(--blue);border:2px solid #fff;width:126px;height:42px;display:flex;align-items:center;justify-content:center;font-size:14px;font-weight:600}
.load{left:511px;top:2325px;width:178px;height:55px;gap:6px}

/* testimonials */
.t-title{left:75px;top:2510px}
.arrows{left:1068px;top:2527px;display:flex;gap:10px}
.quote{position:absolute;width:330px}
.quote p{font-size:14px;font-style:italic;line-height:27px}
.quote h4{font-size:19px;font-weight:700;margin-top:14px}
.stars{display:flex;gap:7px;margin-top:4px}

/* footer */
.footer-photo{left:0;top:2860px;width:1200px;height:526px;background:linear-gradient(160deg,#23272e 0%,#1c2026 50%,#15181c 100%)}
.f-brand{left:72px;top:3082px;color:var(--yellow);font-size:37px;font-weight:700;line-height:43px}
.f-info{left:75px;top:3172px;font-size:13px;line-height:24px}
.f-col{position:absolute;top:3072px}
.f-col h5{color:var(--blue);font-size:20px;font-weight:700;margin-bottom:10px}
.f-col li{list-style:none;font-size:13px;line-height:31.5px}
.f-col p{font-size:13px;line-height:23px;width:240px}
.f-input{width:242px;height:46px;border:1px solid #9aa0a6;margin-top:18px;display:flex;align-items:center;padding-left:15px;font-size:13px;color:#c7c7c7}
.f-sub{width:242px;height:46px;margin-top:11px}
.copy{left:75px;top:3334px;font-size:13px}
.social{left:968px;top:3331px;display:flex;gap:14px}
.social span{width:20px;height:20px;border:2px solid #fff;border-radius:50%}
</style>
</head>
<body>

<!-- hero -->
<div class="photo hero-photo" role="img" aria-label="Laptops and tablets on a desk showing architecture website layouts"></div>
<svg class="wave" style="top:560px" width="1200" height="190" viewBox="0 0 1200 190"><path d="M0 35 C90 10 180 12 300 45 C450 85 580 160 720 165 C880 170 1020 110 1200 125 V190 H0 Z" fill="#000"/></svg>

<div class="abs brand">Quellmont Digital</div>
<nav class="abs nav">
  <a class="active">Home</a><a>About Us</a><a>Services</a><a>Portfolio</a><a>Testimonials</a><a>Contact Us</a>
</nav>
<h1 class="abs hero-title">Welcome to<br><span class="hl">Quellmont Digital</span></h1>
<p class="abs hero-sub">Nemo enim ipsam voluptatem quiavoluptas sit aspernatur aut.</p>
<div class="abs btn hero-btn">Learn More</div>

<form class="abs request">
  <h2>Request For Website</h2>
  <div class="field">Enter Email Address</div>
  <div class="field">Upload Image <svg viewBox="0 0 10 10"><path d="M5 0 L9 4 H6 V7 H4 V4 H1 Z M1 8.5 H9 V10 H1 Z" fill="#111"/></svg></div>
  <div class="field">Upload Logos <svg viewBox="0 0 10 10"><path d="M5 0 L9 4 H6 V7 H4 V4 H1 Z M1 8.5 H9 V10 H1 Z" fill="#111"/></svg></div>
  <div class="field">Select brand colors <svg viewBox="0 0 10 10"><path d="M5 0 L8 4 H2 Z M5 10 L8 6 H2 Z" fill="#111"/></svg></div>
  <div class="field msg">Message</div>
  <div class="submit">Submit</div>
</form>

<!-- about -->
<div class="abs about-frame"></div>
<div class="photo about-photo" role="img" aria-label="Woman browsing an online store on a desktop computer"></div>
<h2 class="abs section-title about-title"><span class="uline">About</span> Business<br>&amp; Services</h2>
<p class="abs about-text">Sed ut perspiciatis unde omnis iste natus error sit voluptatem accusantium doloremque laudantium, totam rem aperiam, eaque ipsa quae ab illo inventore veritatis et quasi architecto beatae vitae dicta sunt explicabo. Nemo enim ipsam voluptatem quia voluptas sit aspernatur aut odit aut fugit, sed quia consequuntur magni &nbsp;dolores eos qui ratione voluptatem sequi nesciunt.</p>
<div class="abs btn about-btn">Learn More</div>

<!-- portfolio -->
<div class="abs portfolio-bg"></div>
<svg class="wave" style="top:1228px" width="1200" height="190" viewBox="0 0 1200 190"><path d="M0 0 H1200 V185 C1060 175 930 90 780 55 C640 25 520 35 400 55 C260 78 130 82 0 78 Z" fill="#000"/></svg>

<h2 class="abs section-title pf-title"><span class="uline">Portfolio</span> Showcase</h2>
<div class="abs tabs">
  <div class="tab on">Category 1</div><div class="tab">Category 2</div><div class="tab">Category 3</div><div class="tab">Category 4</div>
</div>

<div class="card sel" style="left:75px;top:1643px">
  <div class="shot" style="background:linear-gradient(135deg,#8fa7bd,#5f7c98)" role="img" aria-label="Website design shown on a desktop monitor">
    <div class="overlay"><div class="more">More Info</div></div>
  </div>
  <h3>Project Heading</h3>
</div>
<div class="card" style="left:435px;top:1643px">
  <div class="shot" style="background:linear-gradient(180deg,#3a5a86,#1f3350 60%,#8a6a4a)" role="img" aria-label="Airport website shown on a laptop"></div>
  <h3>Project Heading</h3>
</div>
<div class="card" style="left:796px;top:1643px">
  <div class="shot" style="background:linear-gradient(180deg,#e6e6e6,#cfcfcf 70%,#a07a55)" role="img" aria-label="Responsive website on desktop, laptop, tablet and phone"></div>
  <h3>Project Heading</h3>
</div>
<div class="card" style="left:75px;top:1968px">
  <div class="shot" style="background:linear-gradient(160deg,#3d6f8e,#2b8bb0 50%,#c9b99a)" role="img" aria-label="Travel booking website shown on a laptop"></div>
  <h3>Project Heading</h3>
</div>
<div class="card" style="left:435px;top:1968px">
  <div class="shot" style="background:linear-gradient(180deg,#8a6a4a,#e8e8ea 30%,#d6d9de)" role="img" aria-label="Online shop website shown on a laptop"></div>
  <h3>Project Heading</h3>
</div>
<div class="card" style="left:796px;top:1968px">
  <div class="shot" style="background:linear-gradient(180deg,#9a7550,#415c7a 30%,#2e4a6a)" role="img" aria-label="Service plans website shown on a laptop"></div>
  <h3>Project Heading</h3>
</div>

<div class="abs btn load">
  <svg width="16" height="16" viewBox="0 0 16 16"><g fill="#000"><circle cx="8" cy="2" r="1.6"/><circle cx="13" cy="5" r="1.4"/><circle cx="13" cy="11" r="1.2"/><circle cx="8" cy="14" r="1.2"/><circle cx="3" cy="11" r="1.1"/><circle cx="3" cy="5" r="1.4"/></g></svg>
  Load More
</div>

<!-- testimonials -->
<h2 class="abs section-title t-title"><span class="uline">Client</span> Testimonials</h2>
<div class="abs arrows">
  <svg width="24" height="24" viewBox="0 0 24 24"><circle cx="12" cy="12" r="10.5" fill="none" stroke="#fff" stroke-width="2.2"/><path d="M6.5 12 L11 7.5 V10.5 H17 V13.5 H11 V16.5 Z" fill="#fff"/></svg>
  <svg width="24" height="24" viewBox="0 0 24 24"><circle cx="12" cy="12" r="10.5" fill="none" stroke="#0677ba" stroke-width="2.2"/><path d="M17.5 12 L13 7.5 V10.5 H7 V13.5 H13 V16.5 Z" fill="#0677ba"/></svg>
</div>

<svg width="0" height="0" style="position:absolute"><defs><path id="star" d="M8 1 L10 6 L15.2 6.2 L11.1 9.4 L12.6 14.6 L8 11.6 L3.4 14.6 L4.9 9.4 L0.8 6.2 L6 6 Z" fill="none" stroke="#fff300" stroke-width="1.4" stroke-linejoin="round"/></defs></svg>

<div class="quote" style="left:76px;top:2603px">
  <p>“ Sed ut perspiciatis unde omnis iste natus error sit voluptatem accusantium doloremque laudantium, totam rem aperiam, eaque ipsa quae ab illo inventore veritatis..”</p>
  <h4>Name Heading</h4>
  <div class="stars"><svg width="16" height="16"><use href="#star"/></svg><svg width="16" height="16"><use href="#star"/></svg><svg width="16" height="16"><use href="#star"/></svg><svg width="16" height="16"><use href="#star"/></svg><svg width="16" height="16"><use href="#star"/></svg></div>
</div>
<div class="quote" style="left:436px;top:2603px">
  <p>“ Sed ut perspiciatis unde omnis iste natus error sit voluptatem accusantium doloremque laudantium, totam rem aperiam, eaque ipsa quae ab illo inventore veritatis..”</p>
  <h4>Name Heading</h4>
  <div class="stars"><svg width="16" height="16"><use href="#star"/></svg><svg width="16" height="16"><use href="#star"/></svg><svg width="16" height="16"><use href="#star"/></svg><svg width="16" height="16"><use href="#star"/></svg><svg width="16" height="16"><use href="#star"/></svg></div>
</div>
<div class="quote" style="left:798px;top:2603px">
  <p>“ Sed ut perspiciatis unde omnis iste natus error sit voluptatem accusantium doloremque laudantium, totam rem aperiam, eaque ipsa quae ab illo inventore veritatis..”</p>
  <h4>Name Heading</h4>
  <div class="stars"><svg width="16" height="16"><use href="#star"/></svg><svg width="16" height="16"><use href="#star"/></svg><svg width="16" height="16"><use href="#star"/></svg><svg width="16" height="16"><use href="#star"/></svg><svg width="16" height="16"><use href="#star"/></svg></div>
</div>

<!-- footer -->
<div class="photo footer-photo" role="img" aria-label="Dimmed photo of a workspace with a desktop computer"></div>
<svg class="wave" style="top:2850px" width="1200" height="170" viewBox="0 0 1200 170"><path d="M0 0 H1200 V25 C1060 20 980 55 860 60 C720 65 620 40 500 70 C360 105 220 150 0 155 Z" fill="#000"/></svg>

<div class="abs f-brand">Quellmont<br>Digital</div>
<div class="abs f-info">48 Larkspur Row, Suite 12,<br>Harbor City 20410, United States<br><span style="display:block;margin-top:4px">+1 555-010-2048</span><span style="display:block;margin-top:2px">hello@quellmontdigital.example</span></div>

<div class="f-col" style="left:344px">
  <h5>Quick Links</h5>
  <ul><li>Sed ut perspiciatis</li><li>Unde omnis iste</li><li>Natus error sit volupt</li><li>Atem accusantium</li><li>Doloremque</li></ul>
</div>
<div class="f-col" style="left:616px">
  <h5>Resources</h5>
  <ul><li>Sed ut perspiciatis</li><li>Unde omnis iste</li><li>Natus error sit volupt</li><li>Atem accusantium</li><li>Doloremque</li></ul>
</div>
<div class="f-col" style="left:884px">
  <h5>Newsletter</h5>
  <p>Rpiciatisnde omnis istetus error sit volupt accusantium</p>
  <div class="f-input">Email Address</div>
  <div class="btn f-sub">Subscribe</div>
</div>

<div class="abs copy">Copyright © 2023. Quellmont Digital.All Right Reserved</div>
<div class="abs social" aria-label="Social links"><span></span><span></span><span></span><span></span><span></span></div>

</body>
</html>
```